Product Sales Website Design - E-commerce - Shopify etc

We have been selling printing equipment for some time now and think that it will be useful to sell the products on the internet, using a simple e-commerce platform, such as shopify etc. There are roughly a few dozen products - so basically, the idea is to have a modern, simple and clean home page. When someone looks at it, they think, this is it - I want to buy here. I am not going to impose any ideas or say how I want it done.

Just so you know, at the moment there are three categories of products. One being printers, scanners and accessories.

I am excited by this whole project and don't want to have good designers backing out because they feel i am imposing restrictions. Feel free to impress me.

Industry/Entity Type

E-Commerce

Requirements
Must have
• integration with an e-commerce platform is a must or show how to integrate, so I can easily introduce further products.

```html
<!DOCTYPE html>
<html lang="en">
<head>
<meta charset="utf-8">
<title>Halden Equipments</title>
<link href="https://fonts.googleapis.com/css2?family=Crimson+Text:ital,wght@0,400;1,400&family=Audiowide&display=swap" rel="stylesheet">
<style>
:root{
  --bar:#2a2a2a;
  --ink:#333333;
  --muted:#8a8a8a;
  --accent:#d93a12;
  --card:#f3f3f3;
  --line:#d6d6d6;
  --tile-frame:#ececec;
  --tile:#3f3f3f;
  --white:#ffffff;
  --icon:#a3a3a3;
  --orange:#f39a1d;
  --amber:#f6b02a;
  --rust:#a8361a;
}
*{margin:0;padding:0;box-sizing:border-box}
html,body{width:1200px;height:1200px;overflow:hidden;background:var(--white)}
body{position:relative;font-family:"Crimson Text",Georgia,serif;color:var(--ink)}
.abs{position:absolute}

.topbar{left:0;top:0;width:1200px;height:40px;background:var(--bar)}
.topbar .account{left:131px;top:8px;font-size:14.5px;color:var(--white)}
.topbar .cart{left:685px;top:8px;font-size:14.5px;color:var(--white)}
.search{left:876px;top:5px;width:218px;height:27px;background:var(--white);border-radius:4px;box-shadow:inset 0 1px 3px rgba(0,0,0,.25)}
.search span{position:absolute;left:17px;top:5px;font-size:12px;font-style:italic;color:#a0a0a0}
.search svg{position:absolute;right:8px;top:4px}

.brand{left:131px;top:65px;font-size:29.5px;color:var(--accent)}
.nav{left:477px;top:73px;display:flex;gap:28.5px;font-size:16.6px;list-style:none}
.nav li{color:var(--ink)}

.band{left:0;top:267px;width:1200px;height:145px;background:var(--bar)}
.hero{left:100px;top:123px;width:1000px;height:416px;overflow:hidden;
  background:
    radial-gradient(ellipse 260px 200px at 90px 90px,rgba(120,30,15,.85),transparent 70%),
    radial-gradient(ellipse 220px 120px at 210px 330px,rgba(40,150,90,.55),transparent 70%),
    radial-gradient(ellipse 300px 180px at 300px 250px,rgba(200,60,30,.6),transparent 70%),
    radial-gradient(ellipse 200px 260px at 640px 300px,rgba(90,90,90,.75),transparent 70%),
    radial-gradient(ellipse 200px 280px at 880px 250px,rgba(70,70,70,.65),transparent 70%),
    radial-gradient(ellipse 160px 140px at 700px 330px,rgba(255,255,255,.55),transparent 70%),
    linear-gradient(110deg,#9a3418 0%,#d8641e 25%,var(--amber) 48%,var(--orange) 100%)}
.hero-title{left:162px;top:443px;font-size:47px;font-style:italic;color:var(--white);text-shadow:0 1px 3px rgba(0,0,0,.35)}
.arrow{top:318px;width:35px;height:46px;background:#111;display:flex;align-items:center;justify-content:center}
.arrow.prev{left:100px}
.arrow.next{left:1065px}

.category{top:556px;width:321px;height:203px;background:var(--tile-frame);padding:8px}
.category .photo{width:100%;height:100%;display:flex;align-items:center;justify-content:center;padding-bottom:16px;
  background:radial-gradient(ellipse 60% 55% at 50% 50%,#1e1e1e,#2c2c2c 55%,var(--tile) 100%)}
.category .label{font-family:"Audiowide",sans-serif;color:var(--white);font-size:18px;border-top:3px solid var(--white);border-bottom:3px solid var(--white);padding:5px 6px 4px;letter-spacing:0}

.product{top:779px;width:218px;height:244px;background:var(--card);border:1px solid #e0e0e0}
.product .thumb{position:absolute;left:8px;top:8px;width:200px;height:151px;background:var(--white);border:1px solid var(--line)}
.product .thumb div{position:absolute;inset:8px;background:radial-gradient(ellipse 48% 42% at 50% 52%,#1f1f1f,#3a3a3a 55%,rgba(255,255,255,0) 100%)}
.product .thumb .phones{background:radial-gradient(ellipse 28% 44% at 50% 50%,#d3237c,#2a2a2a 55%,rgba(255,255,255,0) 100%)}
.product .name{position:absolute;left:13px;top:166px;font-size:15px;text-transform:uppercase;white-space:nowrap}
.product .price{position:absolute;left:12px;top:193px;font-size:16.5px}
.product .was{position:absolute;right:17px;top:193px;font-size:16.5px;color:var(--muted);text-decoration:line-through}

.rule{left:115px;width:970px;height:1px;background:var(--line)}
.footer-links{left:123px;top:1058px;font-size:14.5px;color:var(--muted)}
.social{left:737px;top:1057px;display:flex;gap:9px}
.social span{width:26px;height:26px;border-radius:50%;background:var(--icon);display:flex;align-items:center;justify-content:center}
.social span::after{content:"";width:8px;height:8px;border-radius:50%;background:var(--white)}
.payments{left:122px;top:1120px;display:flex;gap:6px}
.payments span{width:33px;height:20px;border:1px solid #cfcfcf;border-radius:2px}
.copyright{right:123px;top:1110px;font-size:12px;text-align:right;line-height:22px;color:var(--ink)}
.bottombar{left:0;top:1180px;width:1200px;height:20px;background:var(--bar)}
</style>
</head>
<body>
<header>
  <div class="abs topbar">
    <div class="abs account">Sign in or Create an Account</div>
    <div class="abs cart">Your Cart - (0) items - $0.00</div>
    <div class="abs search"><span>To search your item</span>
      <svg width="18" height="18" viewBox="0 0 18 18"><circle cx="11" cy="7" r="5" fill="none" stroke="#bbb" stroke-width="1.6"/><line x1="7.5" y1="10.5" x2="2" y2="16" stroke="#bbb" stroke-width="2"/></svg>
    </div>
  </div>
  <div class="abs brand">Halden Equipments</div>
  <ul class="abs nav"><li>Home</li><li>About Us</li><li>Categories</li><li>Printers</li><li>Scanners</li><li>Accessories</li><li>Contact Us</li></ul>
</header>

<section>
  <div class="abs band"></div>
  <div class="abs hero" role="img" aria-label="Colourful curled paper sheets with tablets, coffee cup and office papers"></div>
  <div class="abs hero-title">Halden Equipments</div>
  <div class="abs arrow prev"><svg width="18" height="28" viewBox="0 0 18 28"><polyline points="14,3 4,14 14,25" fill="none" stroke="#fff" stroke-width="4"/></svg></div>
  <div class="abs arrow next"><svg width="18" height="28" viewBox="0 0 18 28"><polyline points="4,3 14,14 4,25" fill="none" stroke="#fff" stroke-width="4"/></svg></div>
</section>

<section>
  <div class="abs category" style="left:98px"><div class="photo" role="img" aria-label="Photo printer printing a landscape"><span class="label">PRINTERS</span></div></div>
  <div class="abs category" style="left:438px"><div class="photo" role="img" aria-label="Flatbed scanner with open lid"><span class="label">SCANNERS</span></div></div>
  <div class="abs category" style="left:779px"><div class="photo" role="img" aria-label="Battery accessory close-up"><span class="label">ACCESSORIES</span></div></div>
</section>

<section>
  <article class="abs product" style="left:117px"><div class="thumb"><div role="img" aria-label="Flatbed photo scanner"></div></div><div class="name">Orvex Scanner</div><div class="price">$185.00</div><div class="was">Was $250.00</div></article>
  <article class="abs product" style="left:367px"><div class="thumb"><div role="img" aria-label="Document feeder printer"></div></div><div class="name">Kelvo Printer</div><div class="price">$185.00</div><div class="was">Was $250.00</div></article>
  <article class="abs product" style="left:617px"><div class="thumb"><div role="img" aria-label="All-in-one printer and scanner"></div></div><div class="name">Orvex Printer &amp; Scanner</div><div class="price">$185.00</div><div class="was">Was $250.00</div></article>
  <article class="abs product" style="left:866px"><div class="thumb"><div class="phones" role="img" aria-label="Pink and black headphones"></div></div><div class="name">Headphone</div><div class="price">$185.00</div><div class="was">Was $250.00</div></article>
</section>

<footer>
  <div class="abs rule" style="top:1042px"></div>
  <div class="abs footer-links">SEARCH / ABOUT US</div>
  <div class="abs social"><span></span><span></span><span></span><span></span><span></span><span></span><span></span><span></span><span></span><span></span></div>
  <div class="abs rule" style="top:1094px"></div>
  <div class="abs payments">
    <span style="background:#3d7fc4"></span><span style="background:#e4e4e4"></span><span style="background:#f0e6d6"></span><span style="background:#eef1f5"></span><span style="background:#2f6fb5"></span><span style="background:#d9453a"></span><span style="background:#e8eef6"></span><span style="background:#f2f2f2"></span>
  </div>
  <div class="abs copyright">© 2014.WWW.COMPANY NAME.COM<br>ALL RIGHTS RESERVED</div>
  <div class="abs bottombar"></div>
</footer>
</body>
</html>
```